Recruiting ad for Caregivers and Nurses

We need a few amazing, fun, catchy, creative recruiting ads for Caregivers and Nurses to care for homecare patients on the island of Oahu, in Hawaii. We are an in home care company called Parkdale Homecare. Our care services are provided 24/7, so we need staff that can work days, nights, weekdays, weekends. We need catchy fun ads to entice caregivers and nurses to call our office to inquire about jobs available. Our patients age range is from babies to seniors. We need caregivers and nurses for basic patient care (bathing, dressing, ambulating, preparing meals, medication reminders, light housekeeping) and complex patients (oxygen, tube feeding, injections, vents, wound care). Here are some bullets to consider including:
*Full-time and Part-time Positions Available (days, nights, weekdays, weekends)
*Sign-On Bonus Programs Offered up to $500
*Refer a Friend Bonus Program
*Holiday Pay
*2 Health Plans to Choose from
*Island-Wide Locations
*All PPE Provided (masks, gloves, etc)
*401K Program
*Tuition Benefits

```html
<!DOCTYPE html>
<html lang="en">
<head>
<meta charset="utf-8">
<title>Parkdale Homecare – Caregivers Wanted</title>
<link rel="stylesheet" href="https://fonts.googleapis.com/css2?family=Montserrat:ital,wght@0,400;0,600;0,700;0,800;1,400&family=Nanum+Brush+Script&display=swap">
<style>
  :root {
    --salmon: #f4a287;
    --teal: #0a6f63;
    --panel: #f1f1f1;
    --ink: #3d3d3d;
    --white: #ffffff;
  }
  * { margin: 0; padding: 0; box-sizing: border-box; }
  html, body { width: 927px; height: 1200px; overflow: hidden; background: var(--panel); }
  .flyer {
    position: relative;
    width: 927px;
    height: 1200px;
    overflow: hidden;
    font-family: "Montserrat", sans-serif;
    color: var(--ink);
    background: var(--panel);
  }
  .hero-photo {
    position: absolute; left: 0; top: 0; width: 927px; height: 620px;
    background: linear-gradient(100deg, #eef1f4 0%, #dfe6ee 25%, #4f7fc0 45%, #e9e4de 65%, #8a8466 85%, #c9c4b8 100%);
  }
  .shapes { position: absolute; left: 0; top: 0; width: 927px; height: 1200px; }

  .bonus-badge {
    position: absolute; left: 102px; top: 0; width: 152px; height: 155px;
    background: var(--salmon); color: var(--white);
    border-radius: 0 0 38px 38px;
    text-align: center; font-weight: 800; line-height: 1;
    padding-top: 26px;
  }
  .bonus-badge .label { font-size: 12px; letter-spacing: 0.2px; }
  .bonus-badge .amount { font-size: 33px; margin-top: 8px; }
  .bonus-badge .amount + .amount { font-size: 38px; margin-top: 1px; }

  .headline-script {
    position: absolute; left: 100px; top: 180px;
    font-family: "Nanum Brush Script", cursive;
    font-size: 190px; line-height: 1; color: var(--salmon);
    letter-spacing: 2px;
  }
  .tagline {
    position: absolute; left: 217px; top: 346px; width: 321px; height: 40px;
    background: var(--teal);
    clip-path: polygon(4% 0, 100% 0, 96% 100%, 0 100%);
    color: var(--white); font-weight: 700; font-style: italic;
    font-size: 16px; letter-spacing: 4.5px;
    display: flex; align-items: center; padding-left: 26px;
  }

  .jobs-title {
    position: absolute; left: 420px; top: 616px; width: 470px;
    font-size: 43px; font-weight: 700; line-height: 1.08;
    color: var(--salmon); text-align: right;
  }
  .jobs-copy {
    position: absolute; left: 424px; top: 729px; width: 460px;
    font-size: 13.4px; line-height: 18.3px; text-align: justify;
  }

  .services-title {
    position: absolute; left: 62px; top: 686px;
    font-size: 22px; font-weight: 700; letter-spacing: 2.6px;
    line-height: 30px; color: var(--teal);
  }
  .benefits { position: absolute; left: 58px; top: 770px; list-style: none; }
  .benefits li {
    display: flex; align-items: center; height: 43.4px;
    font-size: 13.5px; font-style: italic; letter-spacing: 1.8px;
  }
  .benefits svg { width: 28px; height: 20px; margin-right: 20px; flex: none; }

  .details { position: absolute; left: 514px; top: 851px; list-style: none; }
  .details li { display: flex; align-items: flex-start; font-size: 14px; line-height: 18px; }
  .details li + li { margin-top: 22px; }
  .details .icon {
    width: 32px; height: 32px; border-radius: 50%; background: var(--salmon);
    flex: none; margin-right: 14px; display: flex; align-items: center; justify-content: center;
    color: var(--white); font-weight: 800; font-size: 18px;
  }
  .details .text { padding-top: 6px; }
  .details li.hours .text { padding-top: 0; margin-top: -2px; }

  .brand-box {
    position: absolute; left: 60px; top: 1065px; width: 135px; height: 115px;
    background: var(--white);
    display: flex; flex-direction: column; align-items: center; justify-content: center;
    color: var(--teal); font-weight: 600; text-align: center;
  }
  .brand-box .mark { width: 22px; height: 22px; background: var(--teal); margin-bottom: 8px; }
  .brand-box .name { font-size: 15px; line-height: 1.2; }

  .contact { position: absolute; left: 227px; top: 1113px; color: var(--white); }
  .contact .label { font-size: 14px; font-weight: 700; font-style: italic; letter-spacing: 4px; }
  .contact .phone { font-size: 24px; font-weight: 700; letter-spacing: 5px; margin-top: 5px; }

  .social { position: absolute; left: 723px; top: 1133px; display: flex; gap: 14px; }
  .social span { width: 34px; height: 34px; border-radius: 50%; background: var(--salmon); }
</style>
</head>
<body>
<div class="flyer">
  <div class="hero-photo" role="img" aria-label="Photo of a smiling caregiver in blue scrubs talking with a smiling senior woman"></div>

  <svg class="shapes" viewBox="0 0 927 1200" aria-hidden="true">
    <path fill="var(--salmon)" d="M0,505 C90,565 210,612 330,602 C430,594 490,550 560,505 L560,640 L0,640 Z"/>
    <path fill="var(--teal)" d="M430,545 C540,470 740,430 927,440 L927,960 L700,960 Z"/>
    <path fill="var(--panel)" d="M0,548 C100,598 230,616 350,600 C470,584 560,505 700,486 C800,474 880,494 905,530 L905,880 C880,990 790,1060 680,1100 L0,1100 Z"/>
    <path fill="var(--salmon)" d="M560,1108 C720,1100 860,1020 927,905 L927,1000 C880,1060 760,1100 640,1110 Z"/>
    <path fill="var(--teal)" d="M0,1068 C200,1058 400,1092 570,1104 C720,1112 860,1050 927,975 L927,1200 L0,1200 Z"/>
  </svg>

  <div class="bonus-badge">
    <div class="label">SIGN-ON BONUS</div>
    <div class="amount">UP TO</div>
    <div class="amount">$500</div>
  </div>

  <div class="headline-script">Caregivers</div>
  <div class="tagline">WE WANT YOU!</div>

  <h2 class="services-title">Our Services<br>Holiday Package.</h2>
  <ul class="benefits">
    <li><svg viewBox="0 0 28 20"><path d="M3,9 L11,17 L25,3" fill="none" stroke="var(--salmon)" stroke-width="4" stroke-linecap="round" stroke-linejoin="round"/></svg>Refer a Friend Bonus Program</li>
    <li><svg viewBox="0 0 28 20"><path d="M3,9 L11,17 L25,3" fill="none" stroke="var(--salmon)" stroke-width="4" stroke-linecap="round" stroke-linejoin="round"/></svg>Holiday Pay</li>
    <li><svg viewBox="0 0 28 20"><path d="M3,9 L11,17 L25,3" fill="none" stroke="var(--salmon)" stroke-width="4" stroke-linecap="round" stroke-linejoin="round"/></svg>2 Health Plans to Choose from</li>
    <li><svg viewBox="0 0 28 20"><path d="M3,9 L11,17 L25,3" fill="none" stroke="var(--salmon)" stroke-width="4" stroke-linecap="round" stroke-linejoin="round"/></svg>All PPE Provided (masks, gloves, etc)</li>
    <li><svg viewBox="0 0 28 20"><path d="M3,9 L11,17 L25,3" fill="none" stroke="var(--salmon)" stroke-width="4" stroke-linecap="round" stroke-linejoin="round"/></svg>401K Program</li>
    <li><svg viewBox="0 0 28 20"><path d="M3,9 L11,17 L25,3" fill="none" stroke="var(--salmon)" stroke-width="4" stroke-linecap="round" stroke-linejoin="round"/></svg>Tuition Benefits</li>
  </ul>

  <h1 class="jobs-title">Jobs Available For Basic Patient Care</h1>
  <p class="jobs-copy">Patients ages range from Babies to Seniors. Basic care needs include bathing, dressing, ambulating, preparing meals, medication reminders and light housekeeping. For complex patients, responsibilites include oxygen, tube feeding, injections, vents and wound care.</p>

  <ul class="details">
    <li><span class="icon"><svg width="16" height="18" viewBox="0 0 16 18"><path d="M8,1 C4,1 1.5,4 1.5,7 C1.5,11 8,17 8,17 C8,17 14.5,11 14.5,7 C14.5,4 12,1 8,1 Z" fill="none" stroke="#fff" stroke-width="2.2"/><circle cx="8" cy="7" r="2.2" fill="#fff"/></svg></span><span class="text">Island-Wide Locations in Hawaii</span></li>
    <li class="hours"><span class="icon">$</span><span class="text">Full-time and Part-time Positions Available<br>(Days, Nights, Weekdays and Weekends)</span></li>
    <li><span class="icon"><svg width="16" height="16" viewBox="0 0 16 16"><circle cx="6.5" cy="6.5" r="4.5" fill="none" stroke="#fff" stroke-width="2.4"/><path d="M10,10 L14.5,14.5" stroke="#fff" stroke-width="2.8" stroke-linecap="round"/></svg></span><span class="text">www.parkdalecare.com</span></li>
  </ul>

  <div class="brand-box">
    <span class="mark"></span>
    <span class="name">Parkdale<br>Homecare</span>
  </div>

  <div class="contact">
    <div class="label">CALL US:</div>
    <div class="phone">808-555-0142</div>
  </div>

  <div class="social" aria-label="Social media links">
    <span></span><span></span><span></span>
  </div>
</div>
</body>
</html>
```